Banner Ad Design Project for Muslim Fashion Site

I need banner ads for an e-commerce site selling modern muslim fashion, called "Velunora.com". It is a flash sale site selling top designer brands of muslim fashion. The key driver of purchase is accessing special sale events for members, which goes up to 90% discount on certain brands.

We would like our logo "velunora.com" to be part of the visual. You can get this logo on the top right of our site landing page (velunora.com). The main visual should show an attractive lady with a modern looking hijab, if possible, with eye contact to the user, but not mandatory.

I am looking at very minimum 5 types of banner ad sizes:
728 x 90
120 x 600
300x 250
234 x 60
125 x125

3 concept variations are required.

Target Market(s)

asian modern muslim woman

Industry/Entity Type

E-Commerce

Requirements
Must have
• velunora.com logo
attractive woman wearing modern looking hijab
the number "90%" to represent the discount on offer
the word "click here" as a call to action

```html
<!DOCTYPE html>
<html lang="en">
<head>
<meta charset="utf-8">
<title>Velunora.com – Banner Set</title>
<link rel="stylesheet" href="https://fonts.googleapis.com/css2?family=Arimo:wght@400;500;700&family=Roboto+Condensed:wght@400&display=swap">
<style>
  :root {
    --canvas: #c2d6d8;
    --ink: #0b0b0b;
    --brand-teal: #5fd0c4;
    --square-dark: #3c4644;
    --square-bg: #418277;
    --cta-pale: #96b3a6;
    --medium-top: #2f4f45;
    --medium-bg: #6fa98c;
    --leader-dark: #233837;
    --leader-bg: #5e9b86;
    --bubble: #8fcbb6;
    --bubble-text: #6b2a15;
    --sky-dark: #202a29;
    --sky-bg: #6f978a;
    --sky-cta: #050505;
    --sky-cta-text: #efd9a7;
    --art-red: #cf3a46;
    --art-deep: #b0262c;
    --art-orange: #d35a30;
  }
  * { box-sizing: border-box; margin: 0; padding: 0; }
  html, body { width: 1200px; height: 1000px; overflow: hidden; }
  body {
    position: relative;
    background: var(--canvas);
    font-family: "Arimo", Arial, sans-serif;
    color: var(--ink);
  }
  .banner { position: absolute; overflow: hidden; }
  .block { position: absolute; }
  .text { position: absolute; white-space: nowrap; line-height: 1; font-weight: 500; }

  .brand {
    position: absolute;
    display: flex;
    align-items: center;
    gap: 8px;
    color: var(--brand-teal);
    font-family: "Arimo", Arial, sans-serif;
    font-weight: 400;
    white-space: nowrap;
    line-height: 1;
  }
  .brand-dot {
    width: 10px; height: 10px; border-radius: 50%;
    background: var(--brand-teal);
    flex: none;
  }

  .model-art {
    position: absolute;
    background: linear-gradient(165deg, var(--art-red) 0%, var(--art-deep) 65%, var(--art-orange) 100%);
  }

  /* Square banner */
  .square { left: 0; top: 0; width: 598px; height: 498px; background: var(--square-bg); }
  .square .brand-panel { left: 0; top: 0; width: 415px; height: 205px; background: var(--square-dark); }
  .square .brand { left: 30px; top: 76px; font-size: 48px; }
  .square .cta { left: 389px; top: 55px; width: 209px; height: 128px; background: var(--cta-pale); }
  .square .cta-text { left: 43px; top: 4px; font-size: 48px; line-height: 1.4; white-space: normal; width: 160px; }
  .square .headline { left: 25px; top: 208px; font-size: 54px; line-height: 77px; word-spacing: 8px; }
  .square .tagline-1 { left: 14px; top: 408px; font-size: 28px; letter-spacing: 1.2px; }
  .square .tagline-2 { left: 82px; top: 456px; font-size: 28px; letter-spacing: 1.2px; }
  .square .model-art { left: 355px; top: 258px; width: 243px; height: 240px; }

  /* Medium banner */
  .medium { left: 625px; top: 329px; width: 350px; height: 349px; background: var(--medium-bg); }
  .medium .brand-panel { left: 0; top: 0; width: 350px; height: 134px; background: var(--medium-top); }
  .medium .brand { left: 12px; top: 58px; font-size: 42px; }
  .medium .cta { left: 0; top: 108px; width: 135px; height: 111px; background: var(--cta-pale); }
  .medium .cta-text { left: 13px; top: 10px; font-size: 38px; line-height: 1.45; white-space: normal; width: 120px; }
  .medium .offer { left: 12px; top: 240px; font-size: 22px; line-height: 33px; white-space: normal; width: 120px; font-weight: 400; }
  .medium .model-art { left: 138px; top: 111px; width: 212px; height: 238px; }

  /* Leaderboard */
  .leader { left: 0; top: 773px; width: 960px; height: 117px; background: var(--leader-bg); }
  .leader .brand-panel { left: 0; top: 0; width: 240px; height: 117px; background: var(--leader-dark); }
  .leader .brand { left: 24px; top: 54px; font-size: 30px; }
  .leader .headline { left: 252px; top: 10px; font-size: 32px; word-spacing: 6px; }
  .leader .tagline-1 { left: 252px; top: 60px; font-size: 20px; letter-spacing: 0.3px; }
  .leader .tagline-2 { left: 302px; top: 80px; font-size: 20px; letter-spacing: 0.3px; }
  .leader .bubble { left: 500px; top: 45px; }
  .leader .bubble-text { left: 538px; top: 63px; font-size: 31px; font-weight: 700; color: var(--bubble-text); }
  .leader .model-art { left: 745px; top: 0; width: 160px; height: 117px; }

  /* Skyscraper */
  .sky { left: 1000px; top: 0; width: 200px; height: 1000px; background: var(--sky-bg); font-family: "Roboto Condensed", "Arial Narrow", sans-serif; }
  .sky .brand-panel { left: 0; top: 0; width: 200px; height: 125px; background: var(--sky-dark); }
  .sky .brand { left: 6px; top: 50px; font-size: 25px; gap: 6px; }
  .sky .brand-dot { width: 8px; height: 8px; }
  .sky .model-art { left: 10px; top: 125px; width: 190px; height: 173px; }
  .sky .text { font-weight: 400; }
  .sky .line-upto { left: 18px; top: 326px; font-size: 52px; font-family: "Arimo", Arial, sans-serif; }
  .sky .line-pct { left: 18px; top: 403px; font-size: 50px; font-family: "Arimo", Arial, sans-serif; }
  .sky .line-disc { left: 4px; top: 456px; font-size: 45px; }
  .sky .line-on { left: 0; width: 200px; text-align: center; top: 518px; font-size: 29px; }
  .sky .line-mm { left: 8px; top: 555px; font-size: 31px; }
  .sky .line-fi { left: 14px; top: 601px; font-size: 31px; }
  .sky .cta { left: 0; top: 755px; width: 200px; height: 125px; background: var(--sky-cta); }
  .sky .cta-text { left: 0; width: 200px; text-align: center; top: 45px; font-size: 31px; color: var(--sky-cta-text); }
</style>
</head>
<body>

  <section class="banner square" aria-label="Square banner">
    <div class="block brand-panel">
      <div class="brand"><span class="brand-dot"></span>Velunora.com</div>
    </div>
    <div class="block cta"><span class="text cta-text">Click Here!</span></div>
    <p class="text headline">UP TO 90%<br>DISCOUNT</p>
    <p class="text tagline-1">Modern Muslim Fassion</p>
    <p class="text tagline-2">&amp; Designer Brands</p>
    <div class="model-art" role="img" aria-label="Illustration of a woman wearing a red and orange hijab"></div>
  </section>

  <section class="banner medium" aria-label="Medium rectangle banner">
    <div class="block brand-panel">
      <div class="brand"><span class="brand-dot"></span>Velunora.com</div>
    </div>
    <div class="block cta"><span class="text cta-text">Click Here!</span></div>
    <p class="text offer">UP TO<br>90%<br>DISCOUNT</p>
    <div class="model-art" role="img" aria-label="Illustration of a woman wearing a red and orange hijab"></div>
  </section>

  <section class="banner leader" aria-label="Leaderboard banner">
    <div class="block brand-panel">
      <div class="brand"><span class="brand-dot"></span>Velunora.com</div>
    </div>
    <p class="text headline">UP TO 90% DISCOUNT</p>
    <p class="text tagline-1">Modern Muslim Fassion</p>
    <p class="text tagline-2">&amp; Designer Brands</p>
    <svg class="block bubble" width="260" height="70" viewBox="0 0 260 70" aria-hidden="true">
      <path d="M126 6 C186 6 234 14 234 34 C234 54 186 62 126 62 C66 62 18 54 18 34 C18 14 66 6 126 6 Z M232 40 L258 36 L230 30 Z" fill="var(--bubble)"/>
    </svg>
    <span class="text bubble-text">Click Here!</span>
    <div class="model-art" role="img" aria-label="Illustration of a woman wearing a red and orange hijab"></div>
  </section>

  <section class="banner sky" aria-label="Skyscraper banner">
    <div class="block brand-panel">
      <div class="brand"><span class="brand-dot"></span>Velunora.com</div>
    </div>
    <div class="model-art" role="img" aria-label="Illustration of a woman wearing a red and orange hijab"></div>
    <p class="text line-upto">UP TO</p>
    <p class="text line-pct">90%</p>
    <p class="text line-disc">DISCOUNT</p>
    <p class="text line-on">on</p>
    <p class="text line-mm">Modern Muslim</p>
    <p class="text line-fi">Fashion Items</p>
    <div class="block cta"><span class="text cta-text">CLICK HERE</span></div>
  </section>

</body>
</html>
```